Brovanta a national investment company

We need a logo/letterhead design to describe our business. We use our business across the country to buy and sale property, buy property mineral rights, make investments in small businesses. Our business goal is to promotes integrity, security and growth in small investments. We want our product to reflect our goals.
Updates
I "think" I want a modern, sleek, not too busy design. I "think" I want a dark green and black/grey colors. However, y'all know best and I am looking forward to seeing your creativity in our design. Thanks for accepting our project. -Delia
We are pleased with some of the designs submitted. We would like for the designs to reflect our company name as it appears on our license, Brovanta. We appreciate the designers who took into consideration our colors we specified. Thanks for all the hard work. We will make a decision tomorrow. You still have time to submit more ideas.
Industry/Entity Type
Investment
Logo Text
Brovanta LLC
Look and feel
Each slider illustrates characteristics of the customer's brand and the style your logo design should communicate.

```html
<!DOCTYPE html>
<html lang="en">
<head>
<meta charset="UTF-8">
<title>Brovanta Letterhead</title>
<link href="https://fonts.googleapis.com/css2?family=Archivo+Black&family=Arimo:wght@400;700&display=swap" rel="stylesheet">
<style>
  :root {
    --backdrop: #e9eaec;
    --paper: #fbfbfb;
    --tint: #f3ede4;
    --brand-green: #3f8f1c;
    --accent-orange: #ec7a1c;
    --ink-black: #1a1a1a;
    --ink-white: #ffffff;
  }
  * { margin: 0; padding: 0; box-sizing: border-box; }
  html, body {
    width: 1200px;
    height: 943px;
    overflow: hidden;
    background: var(--backdrop);
  }
  .canvas {
    width: 1200px;
    height: 943px;
    display: flex;
    align-items: center;
    justify-content: center;
  }
  .letterhead {
    position: relative;
    width: 630px;
    height: 891px;
    background: var(--paper);
    box-shadow: 0 6px 24px rgba(0,0,0,0.12);
    overflow: hidden;
    font-family: "Arimo", Arial, sans-serif;
  }
  .background-tint {
    position: absolute;
    right: 0;
    bottom: 0;
    width: 380px;
    height: 520px;
    background: var(--tint);
    opacity: 0.8;
  }
  .brand {
    position: absolute;
    top: 46px;
    left: 44px;
  }
  .brand-row {
    display: flex;
    align-items: center;
    gap: 10px;
  }
  .brand-mark {
    width: 22px;
    height: 22px;
    background: var(--brand-green);
  }
  .brand-name {
    font-family: "Archivo Black", Arial, sans-serif;
    font-size: 30px;
    color: var(--brand-green);
    letter-spacing: 0.5px;
    line-height: 1;
  }
  .brand-tagline {
    margin-top: 5px;
    font-size: 8.5px;
    letter-spacing: 1px;
    color: var(--accent-orange);
    text-transform: uppercase;
  }
  .contact-list {
    position: absolute;
    right: 36px;
    bottom: 40px;
    list-style: none;
    display: flex;
    flex-direction: column;
    align-items: flex-end;
    gap: 6px;
  }
  .contact-item {
    position: relative;
    display: flex;
    align-items: center;
    gap: 6px;
    height: 20px;
    padding: 0 12px 0 14px;
    background: var(--accent-orange);
    color: var(--ink-white);
    font-size: 11px;
    clip-path: polygon(10px 0, 100% 0, 100% 100%, 0 100%);
  }
  .contact-item::before {
    content: "";
    position: absolute;
    left: 0;
    top: 0;
    width: 10px;
    height: 20px;
    background: var(--ink-black);
    clip-path: polygon(10px 0, 10px 100%, 0 100%);
  }
  .contact-item::after {
    content: "";
    position: absolute;
    right: 0;
    top: 0;
    width: 8px;
    height: 8px;
    background: var(--ink-black);
    clip-path: polygon(0 0, 100% 0, 100% 100%);
  }
  .contact-item:nth-child(1) { margin-right: 60px; }
  .contact-item:nth-child(2) { margin-right: 40px; }
  .contact-item:nth-child(3) { margin-right: 20px; }
  .contact-icon {
    width: 11px;
    height: 11px;
    flex: none;
  }
</style>
</head>
<body>
<main class="canvas">
  <article class="letterhead">
    <div class="background-tint"></div>

    <header class="brand">
      <div class="brand-row">
        <span class="brand-mark"></span>
        <span class="brand-name">BROVANTA</span>
      </div>
      <p class="brand-tagline">A National Investment Company</p>
    </header>

    <ul class="contact-list">
      <li class="contact-item">
        <svg class="contact-icon" viewBox="0 0 12 12"><circle cx="6" cy="6" r="6" fill="#1a1a1a"/><path d="M4 3.2l1 1-.6.8a4 4 0 0 0 1.8 1.8l.8-.6 1 1-.8.9C5.4 8 4 6.6 3.2 4z" fill="#fff"/></svg>
        <span>02 4417 2650</span>
      </li>
      <li class="contact-item">
        <svg class="contact-icon" viewBox="0 0 12 12"><circle cx="6" cy="6" r="6" fill="#1a1a1a"/><rect x="3" y="4" width="6" height="4.2" fill="none" stroke="#fff" stroke-width="0.9"/><path d="M3 4l3 2.4L9 4" fill="none" stroke="#fff" stroke-width="0.9"/></svg>
        <span>info@brovanta.com</span>
      </li>
      <li class="contact-item">
        <svg class="contact-icon" viewBox="0 0 12 12"><circle cx="6" cy="6" r="6" fill="#1a1a1a"/><circle cx="6" cy="6" r="3.2" fill="none" stroke="#fff" stroke-width="0.9"/><path d="M2.8 6h6.4M6 2.8v6.4" stroke="#fff" stroke-width="0.7"/></svg>
        <span>www.brovanta.com</span>
      </li>
      <li class="contact-item">
        <svg class="contact-icon" viewBox="0 0 12 12"><circle cx="6" cy="6" r="6" fill="#1a1a1a"/><path d="M6 9.4L3.8 6.2A2.4 2.4 0 1 1 8.2 6.2z" fill="#fff"/><circle cx="6" cy="4.9" r="0.8" fill="#1a1a1a"/></svg>
        <span>Address Here address here</span>
      </li>
    </ul>
  </article>
</main>
</body>
</html>
```